Manufacturer's Representative Group needs a clean new Website

We represent and sell a number of suppliers that design and build products used in Biopharmaceutical manufacturing. Our sales region is in the central US. Our customer base is scientific / engineering based - so clean, we organized design with a focus on the products - easy and clear navigation is necessary. We do not sell direct or warehouse product - so e-commerce is not needed. Our customers will use the website for reference on what we do and offer - we will use the site as a platform to present products from each vendor and the home page will be used to capture an overview and draw users deeper into the site. You can view our current site - which needs A LOT of help to get ideas on products represented and types of products

Target Market(s)

Engineers and Pharmaceutical / Bio pharm end users

Industry/Entity Type

E-Commerce

Number of Pages Required

2 page

Font styles to use
Sans Serif

Requirements
Must have
• I need a home page that provides a snapshot of my company and the product lines we represent - then a second page that I can copy as a template for each line I rep as well as for an "About us / contact" page.
• I would like to be able to manage content on the pages so something easy to adjust pictures or add content is a must
• Must use our logo

```html
<!DOCTYPE html>
<html lang="en">
<head>
<meta charset="utf-8">
<title>Prairie Bio</title>
<link href="https://fonts.googleapis.com/css2?family=Open+Sans:wght@400;600&display=swap" rel="stylesheet">
<style>
:root{
  --page:#f1f1f1;--white:#fff;--ink:#333;--muted:#666;--line:#dcdcdc;
  --orange:#f06a1c;--navy:#2a3a7a;--nav:#2e2e2e;--nav-text:#9a9a9a;
  --foot-top:#3a3a3a;--foot:#444;--foot-text:#cfcfcf;
}
*{margin:0;padding:0;box-sizing:border-box}
html,body{width:727px;height:1200px;overflow:hidden}
body{position:relative;background:var(--page);font-family:"Open Sans",Arial,sans-serif;color:var(--ink)}
.abs{position:absolute}
.header{left:60px;top:0;width:608px;height:64px;background:var(--white);border:1px solid var(--line);border-top:0}
.brand{left:12px;top:20px;font-size:22px;color:var(--navy);display:flex;align-items:center;gap:7px}
.brand i{width:14px;height:14px;background:var(--orange);border-radius:50%;display:block}
.tagline{left:290px;top:29px;font-size:8px;color:#333}
.cta{left:505px;top:22px;width:91px;height:22px;background:var(--orange);color:#fff;font-size:6.5px;display:flex;align-items:center;justify-content:center}
.nav{left:60px;top:64px;width:608px;height:23px;background:linear-gradient(#3c3c3c,#242424);display:flex}
.nav a{color:var(--nav-text);font-size:6.5px;text-decoration:none;display:flex;align-items:center;justify-content:center;width:74px;border-right:1px solid #444}
.nav a.active{color:#fff;background:#1e1e1e;width:64px}
.panel{left:60px;width:608px;background:var(--white);border:1px solid var(--line)}
.hero-img{left:67px;top:102px;width:593px;height:172px;background:linear-gradient(90deg,#d8d8d8,#f2f2f2 60%,#e4e4e4)}
.hero-art{left:100px;top:108px;width:270px;height:160px;background:linear-gradient(120deg,#c93a3a,#4fb6c0 55%,#6a4fc0);border-radius:40px 40px 8px 8px;opacity:.8}
.hero-title{left:388px;top:134px;font-size:30px;color:var(--orange)}
.hero-sub{left:388px;top:176px;font-size:13px;color:#444}
.hero-text{left:388px;top:199px;width:250px;font-size:7px;line-height:13.5px;color:#666}
.hero-arrows{left:618px;top:251px;display:flex;gap:1px}
.hero-arrows span{width:14px;height:14px;background:var(--orange)}
.tab{left:54px;width:110px;height:20px;background:linear-gradient(#3a3a3a,#1a1a1a);color:#fff;font-size:7px;padding-left:18px;display:flex;align-items:center;box-shadow:2px 2px 2px rgba(0,0,0,.3)}
.pager{left:618px;display:flex;gap:4px}
.pager span{width:16px;height:16px;border:1px solid #ccc;background:#fff}
.thumb{width:129px;height:95px;border:1px solid #ddd}
.caption{width:129px;font-size:7px;text-align:center;color:#333}
.post-img{width:118px;height:88px}
.post-title{font-size:10.5px;color:#333}
.post-date{font-size:6px;color:var(--orange)}
.post-text{width:148px;font-size:6px;line-height:12px;color:#555}
.co{top:932px;width:86px;height:59px;border:1px solid #ddd;display:flex;align-items:center;justify-content:center;gap:4px;font-size:8px;font-weight:600;color:var(--navy)}
.co i{width:8px;height:8px;background:#3a8fd0;display:block;border-radius:50%}
.foot-top{left:0;top:1030px;width:727px;height:42px;background:var(--foot-top)}
.foot{left:0;top:1072px;width:727px;height:128px;background:var(--foot)}
.contact{top:1040px;display:flex;gap:9px;color:#fff}
.contact .ico{width:16px;height:16px;background:#8a8a8a;border-radius:3px}
.contact small{display:block;font-size:6.5px;color:#aaa}
.contact b{font-weight:400;font-size:9.5px}
.social{left:553px;top:1043px;display:flex;gap:6px}
.social span{width:17px;height:17px;border-radius:50%;background:#7d7d7d}
.foot-links{left:0;top:1093px;width:727px;text-align:center;font-size:7px;color:var(--foot-text);word-spacing:2px}
.copy{left:0;top:1112px;width:727px;text-align:center;font-size:6.5px;color:#aaa}
.foot-brand{left:0;top:1140px;width:727px;display:flex;justify-content:center;align-items:center;gap:8px;font-size:22px;color:#bbb}
.foot-brand i{width:14px;height:14px;background:#999;border-radius:50%;display:block}
</style>
</head>
<body>
<header>
  <div class="abs header"></div>
  <div class="abs brand" style="left:73px"><i></i>Prairie Bio</div>
  <div class="abs tagline" style="left:350px">PR-BIO NOW REPRESENTING KEYSTONE SOLUTIONS!</div>
  <div class="abs cta" style="left:565px">CONTACT NOW</div>
  <nav class="abs nav">
    <a class="active">HOME</a><a>PRODUCTS</a><a>SERVICES</a><a>COMPANIES</a><a>CERTIFIED</a><a>BLOG</a><a>CONTACT</a>
  </nav>
</header>

<section>
  <div class="abs panel" style="top:94px;height:188px"></div>
  <div class="abs hero-img" role="img" aria-label="Laboratory glassware with coloured liquids"></div>
  <div class="abs hero-art" role="img" aria-label="Flask and test tubes"></div>
  <div class="abs hero-title">Prairie Bio</div>
  <div class="abs hero-sub">Es un hecho establecido hace demasiado</div>
  <div class="abs hero-text">Es un hecho establecido hace demasiado tiempo que un lector se distraerá con el contenido del texto de un sitio mientras que mira su diseño</div>
  <div class="abs hero-arrows"><span></span><span></span></div>
</section>

<section>
  <div class="abs panel" style="top:296px;height:186px"></div>
  <div class="abs tab" style="top:310px">Our Products</div>
  <div class="abs pager" style="top:311px"><span></span><span></span></div>
  <div class="abs thumb" style="left:73px;top:347px;background:linear-gradient(#c43a32,#e2e2e2)" role="img" aria-label="Peristaltic pump"></div>
  <div class="abs thumb" style="left:222px;top:347px;background:linear-gradient(#e8e8e8,#9aa0a8)" role="img" aria-label="Benchtop pump unit"></div>
  <div class="abs thumb" style="left:373px;top:347px;background:linear-gradient(#fafafa,#c9c9c9)" role="img" aria-label="Filling machine"></div>
  <div class="abs thumb" style="left:524px;top:347px;background:radial-gradient(#6a8fc0,#0e2a5a)" role="img" aria-label="Coiled tubing"></div>
  <div class="abs caption" style="left:73px;top:453px">Es un hecho establecido hace</div>
  <div class="abs caption" style="left:222px;top:453px">Es un hecho establecido hace</div>
  <div class="abs caption" style="left:373px;top:453px">Es un hecho establecido hace</div>
  <div class="abs caption" style="left:524px;top:453px">Es un hecho establecido hace</div>
</section>

<section>
  <div class="abs panel" style="top:498px;height:187px"></div>
  <div class="abs tab" style="top:512px">Featured Products</div>
  <div class="abs pager" style="top:513px"><span></span><span></span></div>
  <div class="abs thumb" style="left:73px;top:550px;background:linear-gradient(90deg,#9a9a9a,#b8e04a 50%,#a0a0a0)" role="img" aria-label="Bioreactor system"></div>
  <div class="abs thumb" style="left:222px;top:550px;background:linear-gradient(90deg,#8a8a8a,#b8e04a 50%,#8a8a8a)" role="img" aria-label="Control unit"></div>
  <div class="abs thumb" style="left:373px;top:550px;background:linear-gradient(#fafafa,#cfcfcf)" role="img" aria-label="Filling line"></div>
  <div class="abs thumb" style="left:524px;top:550px;background:linear-gradient(#fafafa,#c4c4c4)" role="img" aria-label="Capping machine"></div>
  <div class="abs caption" style="left:73px;top:655px">Es un hecho establecido hace</div>
  <div class="abs caption" style="left:222px;top:655px">Es un hecho establecido hace</div>
  <div class="abs caption" style="left:373px;top:655px">Es un hecho establecido hace</div>
  <div class="abs caption" style="left:524px;top:655px">Es un hecho establecido hace</div>
</section>

<section>
  <div class="abs panel" style="top:701px;height:166px"></div>
  <div class="abs tab" style="top:714px">Recent Posts</div>
  <div class="abs pager" style="top:716px;left:616px"><span></span><span></span></div>
  <div class="abs post-img" style="left:73px;top:756px;background:linear-gradient(#e6e8ee,#b8bcc8)" role="img" aria-label="Plastic bottles"></div>
  <div class="abs post-title" style="left:206px;top:755px">Es un hecho establecido hace</div>
  <div class="abs post-date" style="left:206px;top:773px">Posted on 27 November 2014</div>
  <div class="abs post-text" style="left:206px;top:786px">Es un hecho establecido hace demasiado tiempo que un lector se distraerá con el contenido del texto de un sitio mientras que mira su diseño. El punto de usar Lorem Ipsum es que tiene una distribución más o menos normal...</div>
  <div class="abs post-img" style="left:374px;top:756px;background:linear-gradient(135deg,#dceaf4,#4ea0d8)" role="img" aria-label="Lab vials"></div>
  <div class="abs post-title" style="left:508px;top:755px">Es un hecho establecido hace</div>
  <div class="abs post-date" style="left:508px;top:773px">Posted on 27 November 2014</div>
  <div class="abs post-text" style="left:508px;top:786px">Es un hecho establecido hace demasiado tiempo que un lector se distraerá con el contenido del texto de un sitio mientras que mira su diseño. El punto de usar Lorem Ipsum es que tiene una distribución más o menos normal...</div>
</section>

<section>
  <div class="abs panel" style="top:882px;height:124px"></div>
  <div class="abs tab" style="top:896px">Companies Represented</div>
  <div class="abs pager" style="top:898px"><span></span><span></span></div>
  <div class="abs co" style="left:74px"><i></i>CleanLoop</div>
  <div class="abs co" style="left:173px">Northgate Polymers</div>
  <div class="abs co" style="left:271px">Harlow Pumps</div>
  <div class="abs co" style="left:370px">Keystone</div>
  <div class="abs co" style="left:468px">Tidewell Hose Co.</div>
  <div class="abs co" style="left:567px"><i></i>Modulon Works</div>
</section>

<footer>
  <div class="abs foot-top"></div>
  <div class="abs foot"></div>
  <div class="abs contact" style="left:78px"><span class="ico"></span><div><small>CALL US :</small><b>(555) 014-2290</b></div></div>
  <div class="abs contact" style="left:214px"><span class="ico"></span><div><small>EMAIL US :</small><b>sales@prairiebio.example</b></div></div>
  <div class="abs contact" style="left:378px"><span class="ico"></span><div><small>LOCATED :</small><b>120 Harbor Lane, Springfield</b></div></div>
  <div class="abs social"><span></span><span></span><span></span><span></span><span></span></div>
  <div class="abs foot-links">Home &nbsp;/&nbsp; Products &nbsp;/&nbsp; Services &nbsp;/&nbsp; Companies &nbsp;/&nbsp; Certified &nbsp;/&nbsp; Blog &nbsp;/&nbsp; Contact</div>
  <div class="abs copy">© Prairie Biosolutions, Corp. All rights reserved.</div>
  <div class="abs foot-brand"><i></i>Prairie Bio</div>
</footer>
</body>
</html>
```